Transport & Storage Company needs a revamp of current card

Would like to keep same colours & basic design but would like to "sharpen" up look of card.

Please remove "The Bright Haulers"

Please add 1800 419 386 on front & back of card

Please add email address on back of card - martin@brackenfreight.com.au

I would like our ABN No - 83 214 976 302 on back of card (which currently has logo only). Logo on back of card can be removed if insufficient space.

Please design another card (same as above) but with Donna Petherick - 0438 562 714, donna@brackenfreight.com.au

I do not want cards to look "too busy" so please re-arrange layout of card if necessary.

Target Market(s)

Transport & Storage

Industry/Entity Type

It Company

Contact Information for Business Card

Please refer to attached current business card

Font styles to use
Other font styles liked:
• Tahoma

Requirements
Must have
• Refer to project decsription
Nice to have
Should not have

```html
<!DOCTYPE html>
<html lang="en">
<head>
<meta charset="utf-8">
<title>Bracken Freight – Business Cards</title>
<link href="https://fonts.googleapis.com/css2?family=Ubuntu:wght@400;500;700&display=swap" rel="stylesheet">
<style>
  :root {
    --bg: #e6e6ea;
    --card-white: #fbfbfb;
    --purple: #8c4ea3;
    --purple-deep: #6d3386;
    --stripe-grey: #6b6b6b;
    --text-white: #ffffff;
    --shadow: rgba(0, 0, 0, 0.18);
  }
  * { margin: 0; padding: 0; box-sizing: border-box; }
  html, body { width: 1200px; height: 900px; overflow: hidden; }
  body {
    background: var(--bg);
    font-family: "Ubuntu", Tahoma, sans-serif;
    position: relative;
  }
  .card {
    position: absolute;
    width: 540px;
    height: 310px;
    background: var(--card-white);
    box-shadow: 0 10px 28px var(--shadow);
    overflow: hidden;
  }
  .card--back { left: 90px; top: 100px; }
  .card--front { left: 570px; top: 490px; }
  .card__shapes { position: absolute; inset: 0; width: 100%; height: 100%; }
  .brand {
    position: absolute;
    right: 34px;
    top: 30px;
    display: flex;
    align-items: center;
    gap: 10px;
  }
  .brand__dot {
    width: 22px; height: 22px;
    border-radius: 50%;
    background: var(--purple);
  }
  .brand__name {
    font-size: 27px;
    font-weight: 700;
    color: var(--purple);
    letter-spacing: 0.2px;
  }
  .abn {
    position: absolute;
    left: 30px;
    bottom: 28px;
    color: var(--text-white);
    font-size: 15px;
    letter-spacing: 0.4px;
  }
  .contact {
    position: absolute;
    left: 30px;
    bottom: 22px;
    color: var(--text-white);
  }
  .contact__name {
    font-size: 21px;
    font-weight: 500;
    letter-spacing: 0.3px;
  }
  .contact__rule {
    display: flex; gap: 4px;
    margin: 7px 0 9px;
  }
  .contact__rule span { height: 3px; background: var(--text-white); }
  .contact__rule span:first-child { width: 22px; }
  .contact__rule span:last-child { width: 10px; }
  .contact__list { list-style: none; }
  .contact__item {
    display: flex; align-items: center; gap: 10px;
    font-size: 13px; line-height: 20px; letter-spacing: 0.8px;
  }
  .contact__item--phone { font-size: 15px; letter-spacing: 2px; }
  .contact__icon { width: 11px; height: 11px; flex: none; }
  .contact__web { font-size: 13px; letter-spacing: 0.6px; margin-top: 2px; }
</style>
</head>
<body>

<section class="card card--back" aria-label="Business card back">
  <svg class="card__shapes" viewBox="0 0 540 310" preserveAspectRatio="none">
    <defs>
      <linearGradient id="backPurple" x1="0" y1="0" x2="1" y2="0">
        <stop offset="0" stop-color="var(--purple)"/>
        <stop offset="1" stop-color="var(--purple-deep)"/>
      </linearGradient>
    </defs>
    <polygon points="0,200 540,118 540,122 0,222" fill="var(--stripe-grey)"/>
    <polygon points="0,234 540,126 540,310 0,310" fill="url(#backPurple)"/>
  </svg>
  <div class="brand">
    <span class="brand__dot"></span>
    <span class="brand__name">Bracken Freight</span>
  </div>
  <p class="abn">ABN No - 83 214 976 302</p>
</section>

<section class="card card--front" aria-label="Business card front">
  <svg class="card__shapes" viewBox="0 0 540 310" preserveAspectRatio="none">
    <defs>
      <linearGradient id="frontPurple" x1="0" y1="0" x2="1" y2="0">
        <stop offset="0" stop-color="var(--purple)"/>
        <stop offset="1" stop-color="var(--purple-deep)"/>
      </linearGradient>
    </defs>
    <polygon points="0,148 540,86 540,90 0,172" fill="var(--stripe-grey)"/>
    <polygon points="0,184 540,94 540,310 0,310" fill="url(#frontPurple)"/>
  </svg>
  <div class="brand">
    <span class="brand__dot"></span>
    <span class="brand__name">Bracken Freight</span>
  </div>
  <div class="contact">
    <p class="contact__name">Martin Ostrowski</p>
    <div class="contact__rule"><span></span><span></span></div>
    <ul class="contact__list">
      <li class="contact__item contact__item--phone">
        <svg class="contact__icon" viewBox="0 0 12 12"><rect x="3" y="0.5" width="6" height="11" rx="1" fill="none" stroke="#fff" stroke-width="1.2"/></svg>
        0451 273 608
      </li>
      <li class="contact__item contact__item--phone">
        <svg class="contact__icon" viewBox="0 0 12 12"><path d="M2 1 L4.5 1 L5.5 3.8 L4 5 Q5.3 7.6 7 8 L8.2 6.5 L11 7.5 L11 10 Q6 11.5 2.5 7 Q0.5 4 2 1 Z" fill="#fff"/></svg>
        1800 419 386
      </li>
      <li class="contact__item">
        <svg class="contact__icon" viewBox="0 0 12 12"><rect x="0.6" y="2.2" width="10.8" height="7.6" fill="none" stroke="#fff" stroke-width="1.2"/><path d="M0.6 2.4 L6 6.8 L11.4 2.4" fill="none" stroke="#fff" stroke-width="1.2"/></svg>
        martin@brackenfreight.com.au
      </li>
    </ul>
    <p class="contact__web">www.brackenfreight.com.au</p>
  </div>
</section>

</body>
</html>
```